Visitenkarten-Design für  Softwareunternehmen
Visitenkarten-Design für Softwareunternehmen
Toller Designer! Ist immer auf Vorschläge eingegangen und hat diese umgesetzt. Bin sehr zufrieden mit dem Ergebnis.
Zielgruppe
Wir sind ein B2B Softwareunternehmen, das eine Energiemonitoringsoftware für die mittelständische Industrie entwickelt hat. Das heißt unsere Visitenkarten werden überwiegend an unsere Zielgruppe, d.h. Geschäftsführer produzierender mittelständischer Industrie ausgehändigt.
Aufgabenstellung
Gleichzeitig treten wir nach außen jung, innovativ und voller Tatendrang auf. Ganz nach unserer Vision: Voll Energie. Null Emission. (Auch gerne auf der Visitenkarte mit aufnehmen). Uns ist es wichtig, unser CI nach außen zu kommunizieren und unsere Webseite auf der Visitenkarte zu platzieren.
Die Visitenkarte soll einzeln für jeden MitarbeiterIn personalisiert werden können.

```html
<!DOCTYPE html>
<html lang="de">
<head>
<meta charset="utf-8">
<title>voltra – Visitenkarte</title>
<link href="https://fonts.googleapis.com/css2?family=Montserrat:wght@300;400;700&display=swap" rel="stylesheet">
<style>
  :root {
    --ink: #283132;
    --paper: #ffffff;
    --stage: #ffffff;
  }
  * { margin: 0; padding: 0; box-sizing: border-box; }
  html, body {
    width: 1200px;
    height: 1199px;
    overflow: hidden;
    background: var(--stage);
    font-family: "Montserrat", sans-serif;
    color: var(--ink);
  }
  .card {
    position: absolute;
    left: 222px;
    width: 762px;
    height: 436px;
  }
  .card--front {
    top: 132px;
    background: var(--paper);
    border: 1px solid #e6e8e8;
  }
  .card--back {
    top: 619px;
    background: var(--ink);
    display: flex;
    align-items: center;
    justify-content: center;
  }
  .wordmark {
    position: absolute;
    right: 48px;
    top: 54px;
    display: flex;
    align-items: center;
    gap: 18px;
    font-weight: 700;
    font-size: 78px;
    line-height: 1;
    letter-spacing: 2px;
    color: var(--ink);
  }
  .wordmark__square {
    width: 26px;
    height: 26px;
    background: var(--ink);
  }
  .person-name {
    position: absolute;
    right: 43px;
    top: 192px;
    font-weight: 300;
    font-size: 38px;
    letter-spacing: 0.3px;
  }
  .contact {
    position: absolute;
    left: 50px;
    top: 276px;
    list-style: none;
    font-size: 18px;
    font-weight: 400;
  }
  .contact li {
    display: flex;
    align-items: center;
    height: 31px;
  }
  .contact svg {
    width: 20px;
    height: 20px;
    margin-right: 8px;
    flex: none;
  }
  .contact .no-icon { padding-left: 28px; }
  .back-wordmark {
    font-weight: 700;
    font-size: 128px;
    letter-spacing: 4px;
    color: var(--paper);
    line-height: 1;
  }
</style>
</head>
<body>
  <section class="card card--front">
    <div class="wordmark"><span class="wordmark__square"></span>voltra</div>
    <div class="person-name">marenholtwig</div>
    <ul class="contact">
      <li>
        <svg viewBox="0 0 20 20" fill="none" stroke="currentColor" stroke-width="1.8"><path d="M10 18s-6-6.2-6-10.5a6 6 0 0 1 12 0C16 11.8 10 18 10 18z"/><circle cx="10" cy="7.5" r="2.2"/></svg>
        Lindengasse 24, 12345 Musterstadt
      </li>
      <li>
        <svg viewBox="0 0 20 20" fill="none" stroke="currentColor" stroke-width="1.8"><rect x="2" y="4.5" width="16" height="11"/><path d="M2 5l8 6 8-6"/></svg>
        marenholtwig@voltra.example
      </li>
      <li>
        <svg viewBox="0 0 20 20" fill="currentColor"><path d="M5.5 2.5l3 3-1.8 2a10 10 0 0 0 5.8 5.8l2-1.8 3 3-2.2 2.3C10 16.5 3.5 10 3.2 4.7z"/></svg>
        015100000000
      </li>
      <li class="no-icon">01234/567-890</li>
    </ul>
  </section>

  <section class="card card--back">
    <div class="back-wordmark">voltra</div>
  </section>
</body>
</html>
```